Business card for femtech company

Nothing too elaborate but elegant and geared towards the mother and baby market. Prefer full-bleed with logo (attached) rear.

```html
<!DOCTYPE html>
<html lang="en">
<head>
<meta charset="utf-8">
<title>Nurvia business card</title>
<link rel="stylesheet" href="https://fonts.googleapis.com/css2?family=Open+Sans:wght@400;600;700&display=swap">
<style>
  :root {
    --page: #e6e7e9;
    --card-dark: #1f1f23;
    --card-dark-tint: #272b2e;
    --teal: #4cc3b5;
    --teal-light: #62d0c3;
    --silver: #b8b8ba;
    --swoosh-grey: #a9a9ab;
    --ink-light: #ececec;
    --rule: #8d8f92;
  }
  * { box-sizing: border-box; margin: 0; padding: 0; }
  html, body {
    width: 1200px; height: 780px; overflow: hidden;
    background: var(--page);
    font-family: "Open Sans", Arial, sans-serif;
  }
  .sheet { position: relative; width: 1200px; height: 780px; }

  .card {
    position: absolute; top: 235px;
    width: 540px; height: 310px;
    overflow: hidden; border-radius: 3px;
    box-shadow: 0 6px 18px rgba(0,0,0,.18);
  }
  .card--front { left: 40px; background: var(--card-dark); }
  .card--back  { left: 620px; }

  /* front */
  .front-decor, .front-swoosh { position: absolute; inset: 0; width: 100%; height: 100%; }

  .brand {
    position: absolute; left: 36px; top: 36px;
    display: flex; align-items: center; gap: 16px;
  }
  .brand__dot {
    width: 50px; height: 50px; border-radius: 50%;
    background: var(--teal);
  }
  .brand__name {
    font-size: 44px; font-weight: 400; letter-spacing: 1px;
    color: var(--silver); line-height: 1;
  }

  .divider {
    position: absolute; left: 22px; right: 32px; top: 134px;
    height: 1px; background: var(--rule);
  }

  .person {
    position: absolute; right: 32px; top: 84px; text-align: right;
  }
  .person__name {
    font-size: 25px; font-weight: 700; color: var(--teal);
    letter-spacing: .5px; line-height: 1.1;
  }
  .person__role {
    font-size: 14px; font-weight: 400; color: var(--ink-light);
    letter-spacing: .6px; margin-top: 2px;
  }

  .contact {
    position: absolute; left: 22px; top: 146px;
    color: var(--ink-light); font-size: 12px; line-height: 1.45;
    letter-spacing: .3px;
  }
  .contact__address { margin-bottom: 6px; }
  .contact__list { list-style: none; }
  .contact__item { display: flex; align-items: center; gap: 6px; }
  .contact__icon { width: 11px; height: 11px; flex: none; }

  /* back */
  .back-pattern {
    position: absolute; inset: 0;
    background: linear-gradient(135deg, var(--teal) 0%, var(--teal) 55%, var(--teal-light) 100%);
  }
  .back-brand {
    position: absolute; left: 320px; top: 216px;
    display: flex; align-items: center; gap: 10px;
  }
  .back-brand__dot {
    width: 26px; height: 26px; border-radius: 50%;
    background: #ffffff;
  }
  .back-brand__name {
    font-size: 20px; font-weight: 400; color: #ffffff; letter-spacing: .8px;
  }
</style>
</head>
<body>
<main class="sheet">

  <section class="card card--front" aria-label="Card front">
    <svg class="front-decor" viewBox="0 0 540 310" aria-hidden="true">
      <circle cx="385" cy="150" r="115" fill="var(--card-dark-tint)"/>
    </svg>

    <svg class="front-swoosh" viewBox="0 0 540 310" aria-hidden="true">
      <path d="M0,246 C170,232 360,254 505,310 L0,310 Z" fill="var(--teal)"/>
      <path d="M0,262 C170,250 350,268 488,310 L0,310 Z" fill="var(--card-dark)"/>
      <path d="M0,272 C170,262 345,278 476,310 L0,310 Z" fill="var(--swoosh-grey)"/>
    </svg>

    <div class="brand">
      <span class="brand__dot"></span>
      <span class="brand__name">Nurvia</span>
    </div>

    <div class="person">
      <p class="person__name">Lena Marsh</p>
      <p class="person__role">Managing Director</p>
    </div>

    <div class="divider"></div>

    <div class="contact">
      <p class="contact__address">Unit 4, Harbour Lane Works,<br>Ringsend, Dublin 4, D04 RX27</p>
      <ul class="contact__list">
        <li class="contact__item">
          <svg class="contact__icon" viewBox="0 0 12 12" aria-hidden="true"><path d="M2.5 1 L4.5 1 L5.3 3.4 L4 4.4 C4.7 5.9 6 7.2 7.6 8 L8.6 6.7 L11 7.5 L11 9.5 C11 10.3 10.3 11 9.5 11 C5 10.6 1.4 7 1 2.5 C1 1.7 1.7 1 2.5 1 Z" fill="var(--teal)"/></svg>
          <span>(555) 014-2290</span>
        </li>
        <li class="contact__item">
          <svg class="contact__icon" viewBox="0 0 12 12" aria-hidden="true"><rect x="1" y="2.5" width="10" height="7" rx="1" fill="none" stroke="var(--teal)" stroke-width="1.2"/><path d="M1.5 3 L6 6.5 L10.5 3" fill="none" stroke="var(--teal)" stroke-width="1.2"/></svg>
          <span>hello@nurvia.com</span>
        </li>
        <li class="contact__item">
          <svg class="contact__icon" viewBox="0 0 12 12" aria-hidden="true"><circle cx="6" cy="6" r="4.8" fill="none" stroke="var(--teal)" stroke-width="1.1"/><ellipse cx="6" cy="6" rx="2" ry="4.8" fill="none" stroke="var(--teal)" stroke-width="1"/><path d="M1.2 6 H10.8" stroke="var(--teal)" stroke-width="1"/></svg>
          <span>www.nurvia.com</span>
        </li>
      </ul>
    </div>
  </section>

  <section class="card card--back" aria-label="Card back">
    <div class="back-pattern" role="img" aria-label="Repeating brand-symbol pattern in darker teal across a teal background"></div>
    <div class="back-brand">
      <span class="back-brand__dot"></span>
      <span class="back-brand__name">Nurvia</span>
    </div>
  </section>

</main>
</body>
</html>
```